Rin3Vox Header

I want a professional Letterhead for my law firm. I'm attaching the letterhead I currently use in Word and PDF form. I'm also attaching my logo, and an example header that I like.

```html
<!DOCTYPE html>
<html lang="en">
<head>
<meta charset="utf-8">
<title>Rin3Vox Letterhead</title>
<link rel="stylesheet" href="https://fonts.googleapis.com/css2?family=Lato:wght@400;700;900&family=Open+Sans:wght@400;600&display=swap">
<style>
  :root {
    --backdrop: #e4e5e7;
    --paper: #ffffff;
    --ink: #444444;
    --ink-dark: #222222;
    --brand-blue: #1a6fc4;
    --band-blue: #1a6fc4;
    --band-green: #3d9a3b;
    --footer-text: #ffffff;
    --sig-tone: #cfd3d8;
  }
  * { margin: 0; padding: 0; box-sizing: border-box; }
  html, body {
    width: 1040px; height: 1200px; overflow: hidden;
    background: var(--backdrop);
  }
  .letterhead {
    position: absolute; left: 71px; top: 23px;
    width: 897px; height: 1153px;
    background: var(--paper);
    box-shadow: 0 4px 18px rgba(0,0,0,.18);
    font-family: "Open Sans", Arial, sans-serif;
    color: var(--ink);
  }
  .firm-name {
    position: absolute; left: 90px; top: 24px;
    font-family: "Lato", Arial, sans-serif; font-weight: 900;
    font-size: 52px; letter-spacing: -1px; color: var(--ink-dark);
  }
  .attorney {
    position: absolute; right: 93px; top: 36px; text-align: right;
    font-family: "Lato", Arial, sans-serif; line-height: 20px;
  }
  .attorney .name { color: var(--brand-blue); font-weight: 700; font-size: 19px; }
  .attorney .title { color: var(--ink-dark); font-size: 16px; }
  .letter { position: absolute; left: 85px; right: 87px; font-size: 14.1px; }
  .issue-date { top: 215px; }
  .recipient { top: 249px; line-height: 17.4px; }
  .salutation { top: 349px; }
  .body-copy { top: 396px; }
  .body-copy p {
    line-height: 25.8px; text-align: justify;
    -webkit-hyphens: auto; hyphens: auto;
  }
  .body-copy p + p { margin-top: 26px; }
  .closing { top: 789px; }
  .signature {
    position: absolute; left: 85px; top: 824px;
    width: 205px; height: 24px; background: var(--sig-tone); border-radius: 3px;
  }
  .signer-name {
    position: absolute; left: 85px; top: 863px;
    font-size: 17px; font-weight: 600; color: var(--ink-dark);
  }
  .signer-role { position: absolute; left: 85px; top: 892px; font-size: 14.1px; }
  .band-blue {
    position: absolute; left: 0; right: 0; top: 1054px; height: 9px; background: var(--band-blue);
  }
  .band-green {
    position: absolute; left: 0; right: 0; top: 1063px; height: 90px; background: var(--band-green);
    font-family: "Lato", Arial, sans-serif; color: var(--footer-text); font-size: 16.5px;
  }
  .contact-row { position: absolute; left: 59px; display: flex; align-items: center; gap: 4px; }
  .contact-row.address { top: 10px; }
  .contact-row.lines { top: 52px; }
  .contact-divider {
    position: absolute; left: 59px; width: 565px; top: 42px; height: 1px; background: rgba(255,255,255,.75);
  }
  .contact-item { display: flex; align-items: center; gap: 4px; margin-right: 3px; }
  .icon { width: 26px; height: 26px; flex: none; }
</style>
</head>
<body>
  <article class="letterhead">
    <div class="firm-name">Rin3Vox</div>
    <div class="attorney">
      <div class="name">Marcus T Delgado III</div>
      <div class="title">Attorney At Law, PLLC</div>
    </div>

    <div class="letter issue-date">Issuing Date: May 5, 2018</div>
    <div class="letter recipient">Name Of Employee Mr. XYZABC<br>Address of Employee<br>Address Line 2 etc..</div>
    <div class="letter salutation">Dear Mr.XYZABC</div>

    <div class="letter body-copy">
      <p>Lorem Ipsum has been the industry's standard dummy text ever since the 1500s, when an unknown printer took a galley of type and scrambled it to make a type specimen book. It has survived not only five centuries, but also the leap into electronic typesetting, remaining essentially unchanged. It was popularised in the 1960s with the release of Lettrina sheets containing Lorem Ipsum passages, and more recently with desktop publishing software like Corvin PageSmith including versions of Lorem Ipsum.</p>
      <p>Lorem Ipsum is simply dummy text of the printing and typesetting industry. Lorem Ipsum has been the industry's standard dummy text ever since the 1500s, when an unknown printer took a galley of type and scrambled it to make a type specimen book.</p>
      <p>It has survived not only five centuries, but also the leap into electronic typesetting, remaining essentially unchanged. It was popularised in the 1960s with the release of Lettrina sheets containing Lorem IpsumIpsum passages.</p>
    </div>

    <div class="letter closing">Yours Sincerely</div>
    <div class="signature" role="img" aria-label="Handwritten signature of Daniel Harper"></div>
    <div class="signer-name">Daniel Harper</div>
    <div class="signer-role">Managing Director</div>

    <div class="band-blue"></div>
    <footer class="band-green">
      <div class="contact-row address">
        <svg class="icon" viewBox="0 0 26 26"><circle cx="13" cy="13" r="12" fill="#fff"/><path d="M13 6a5 5 0 0 0-5 5c0 3.8 5 9 5 9s5-5.2 5-9a5 5 0 0 0-5-5z" fill="var(--band-green)"/><circle cx="13" cy="11" r="2" fill="#fff"/></svg>
        <span>2410 Harlow St. Ste 200 Austin, TX 78701</span>
      </div>
      <div class="contact-divider"></div>
      <div class="contact-row lines">
        <span class="contact-item">
          <svg class="icon" viewBox="0 0 26 26"><circle cx="13" cy="13" r="12" fill="#fff"/><path d="M7 10c0-2 2-3 6-3s6 1 6 3v1h-3V9.5h-6V11H7z M8 12h10l1 6H7z" fill="var(--band-green)"/><circle cx="13" cy="15" r="1.6" fill="#fff"/></svg>
          800.555.0143
        </span>
        <span class="contact-item">
          <svg class="icon" viewBox="0 0 26 26"><circle cx="13" cy="13" r="12" fill="#fff"/><rect x="9" y="6" width="8" height="4" fill="var(--band-green)"/><rect x="7" y="10.5" width="12" height="6" rx="1" fill="var(--band-green)"/><rect x="9" y="15" width="8" height="5" fill="var(--band-green)" stroke="#fff" stroke-width="1"/></svg>
          512.555.0178
        </span>
        <span class="contact-item">
          <svg class="icon" viewBox="0 0 26 26"><circle cx="13" cy="13" r="12" fill="#fff"/><rect x="7" y="8.5" width="12" height="9" fill="var(--band-green)"/><path d="M7.5 9l5.5 4.5L18.5 9" fill="none" stroke="#fff" stroke-width="1.2"/></svg>
          rin@rin3vox.net
        </span>
        <span class="contact-item">
          <svg class="icon" viewBox="0 0 26 26"><circle cx="13" cy="13" r="12" fill="#fff"/><circle cx="13" cy="13" r="6.5" fill="var(--band-green)"/><path d="M10 9.5c1.5.5 2 1.5 1.5 2.5s.5 2 1.5 2.5M15 16.5c.5-1 1.5-1.5 2.5-1" fill="none" stroke="#fff" stroke-width="1.1"/></svg>
          rin3vox.com
        </span>
      </div>
    </footer>
  </article>
</body>
</html>
```